Healthy Supplement featuring Moringa products

Need 3 business card options for our reps to order from Printwell. Our reps will be ordering from Printwell once we upload them. Attached is our current designs to show what info needs to be on the cards. Our website is www.tqvitality.com
The business cards will be a template for our reps to order from. Most of our reps are Asian & Hispanic. Please look at our website so you can see who we are to get the look and feel what we need.
Target Market(s)
Adults 30 on up. Health oriented people.
Industry/Entity Type
Health And Wellness
Contact Information for Business Card
Name
Title
Phone
Logo
www.tqvitality.com/my/username
Font styles to use
Requirements
Must have
- Please match our website look and colors. A moringa leaf is nice, but am open to something different.
Nice to have
- Healthy looking and warm, not super cold or too modern.
Should not have
- No harsh colors please.

```html
<!DOCTYPE html>
<html lang="en">
<head>
<meta charset="utf-8">
<title>TQ Vitality Business Card</title>
<link href="https://fonts.googleapis.com/css2?family=Open+Sans:wght@400;700&family=Roboto+Condensed:wght@300&display=swap" rel="stylesheet">
<style>
  :root {
    --lime: #c8dc2c;
    --leaf: #8dc63f;
    --green: #2bb37c;
    --teal: #3daea0;
    --logo-green: #6aa843;
    --white: #ffffff;
    --hairline: #eef3d8;
  }
  html, body {
    margin: 0;
    padding: 0;
    width: 805px;
    height: 1200px;
    overflow: hidden;
    background: var(--white);
  }
  .sheet { display: block; width: 805px; height: 1200px; }
  .person-name { font-family: "Open Sans", sans-serif; font-weight: 400; fill: var(--white); }
  .person-title { font-family: "Open Sans", sans-serif; font-weight: 700; fill: var(--white); letter-spacing: 4px; }
  .contact-text { font-family: "Roboto Condensed", sans-serif; font-weight: 300; fill: var(--white); }
  .contact-rule { stroke: var(--white); stroke-width: 3; stroke-dasharray: 2 5; stroke-linecap: round; }
  .brand-name { font-family: "Open Sans", sans-serif; font-weight: 700; fill: var(--logo-green); }
  .icon { fill: var(--white); }
  .icon-line { fill: none; stroke: var(--white); stroke-width: 4; }
</style>
</head>
<body>
<svg class="sheet" viewBox="0 0 1355 2050" preserveAspectRatio="none" xmlns="http://www.w3.org/2000/svg">
  <defs>
    <linearGradient id="frontGradient" x1="0" y1="0" x2="1" y2="0">
      <stop offset="0" stop-color="var(--lime)"/>
      <stop offset="0.35" stop-color="var(--leaf)"/>
      <stop offset="0.78" stop-color="var(--green)"/>
      <stop offset="1" stop-color="var(--teal)"/>
    </linearGradient>
    <linearGradient id="backGradient" x1="0" y1="0" x2="1" y2="1">
      <stop offset="0" stop-color="#a6cc39"/>
      <stop offset="0.5" stop-color="#80c350"/>
      <stop offset="1" stop-color="#4fb884"/>
    </linearGradient>
    <linearGradient id="cornerGradient" x1="1" y1="0" x2="0" y2="1">
      <stop offset="0" stop-color="#3db55c"/>
      <stop offset="1" stop-color="var(--leaf)"/>
    </linearGradient>
  </defs>

  <!-- Front card -->
  <g class="card-front">
    <path d="M0,50 Q0,0 50,0 L175,0 C150,110 90,190 0,240 Z" fill="url(#cornerGradient)"/>
    <path d="M0,265 C90,210 150,130 172,40" fill="none" stroke="#5cbb4a" stroke-width="8"/>
    <path d="M530,0 L548,0 C560,320 480,520 370,660 C460,500 545,320 530,0 Z" fill="#72bc45"/>
    <path d="M240,768 C430,680 565,500 598,268 C585,480 470,660 305,768 Z" fill="url(#frontGradient)"/>
    <path d="M592,0 L1205,0 Q1255,0 1255,50 L1255,718 Q1255,768 1205,768 L340,768 C490,650 600,420 592,0 Z" fill="url(#frontGradient)"/>
    <path d="M660,0 L1255,0 L1255,768 L1080,768 Z" fill="#ffffff" opacity="0.12"/>

    <g class="front-brand">
      <circle cx="140" cy="395" r="22" fill="var(--logo-green)"/>
      <text class="brand-name" x="175" y="410" font-size="44">TQ Vitality</text>
    </g>

    <text class="person-name" x="895" y="162" font-size="128" text-anchor="middle">Name</text>
    <line x1="678" y1="174" x2="1144" y2="174" stroke="var(--white)" stroke-width="1.5"/>
    <text class="person-title" x="888" y="226" font-size="50" text-anchor="middle">Title</text>

    <g class="contact-address">
      <path class="icon" d="M694,292 L726,324 L718,324 L718,366 L670,366 L670,324 L662,324 Z"/>
      <rect x="680" y="332" width="11" height="11" rx="3" fill="#6fbf52"/>
      <rect x="697" y="332" width="11" height="11" rx="3" fill="#6fbf52"/>
      <rect x="680" y="347" width="11" height="11" rx="3" fill="#6fbf52"/>
      <rect x="697" y="347" width="11" height="11" rx="3" fill="#6fbf52"/>
      <text class="contact-text" x="755" y="340" font-size="52">Your Address</text>
      <line class="contact-rule" x1="748" y1="356" x2="1134" y2="356"/>
    </g>
    <g class="contact-phone">
      <rect class="icon-line" x="670" y="403" width="42" height="74" rx="6"/>
      <line class="icon-line" x1="672" y1="416" x2="710" y2="416"/>
      <line class="icon-line" x1="672" y1="463" x2="710" y2="463"/>
      <text class="contact-text" x="742" y="448" font-size="48">+99 813555010290</text>
      <line class="contact-rule" x1="745" y1="460" x2="1132" y2="460"/>
    </g>
    <g class="contact-email">
      <rect class="icon" x="658" y="514" width="64" height="54" rx="3"/>
      <path d="M660,518 L690,544 L720,518" fill="none" stroke="#7fc25a" stroke-width="3"/>
      <text class="contact-text" x="744" y="538" font-size="48">hello@tqvitality.com</text>
      <line class="contact-rule" x1="744" y1="563" x2="1130" y2="563"/>
    </g>
    <g class="contact-web">
      <circle cx="691" cy="645" r="30" class="icon"/>
      <g fill="none" stroke="#66ba5a" stroke-width="3">
        <ellipse cx="691" cy="645" rx="13" ry="28"/>
        <line x1="691" y1="617" x2="691" y2="673"/>
        <line x1="663" y1="645" x2="719" y2="645"/>
        <line x1="667" y1="631" x2="715" y2="631"/>
        <line x1="667" y1="659" x2="715" y2="659"/>
      </g>
      <text class="contact-text" x="742" y="650" font-size="48">www.tqvitality.com</text>
      <line class="contact-rule" x1="742" y1="666" x2="1128" y2="666"/>
    </g>
  </g>

  <!-- Back card -->
  <g class="card-back">
    <path d="M170,1277 L1340,1277 L1340,2045 L170,2045 Q118,2045 118,1993 L118,1329 Q118,1277 170,1277 Z" fill="var(--white)" stroke="var(--hairline)" stroke-width="1.5"/>
    <path d="M486,1277 L508,1277 C380,1370 260,1530 234,1730 C250,1530 350,1370 486,1277 Z" fill="#9cc83a"/>
    <path d="M510,1277 L1290,1277 C1270,1620 1180,1880 985,2045 L200,2045 C230,1700 320,1440 510,1277 Z" fill="url(#backGradient)"/>
    <path d="M585,1277 L1290,1277 C1280,1500 1240,1700 1170,1860 L985,2045 Z" fill="#ffffff" opacity="0.12"/>
    <path d="M1255,1590 C1230,1780 1150,1940 1040,2045 L1010,2045 C1130,1940 1220,1790 1255,1590 Z" fill="#b5d35a"/>
    <g class="back-brand">
      <circle cx="590" cy="1680" r="26" fill="var(--logo-green)"/>
      <text class="brand-name" x="632" y="1697" font-size="52">TQ Vitality</text>
    </g>
  </g>
</svg>
</body>
</html>
```